Brightfold Systems, a software development company, needs a website

We need a website to promote our software development company. The company is brand new and we want to market ourselves. We develop all kinds of software from web applications, to desktop applications, to mobile applications. Small company, not a lot of history, just need something flashy.

```html
<!DOCTYPE html>
<html lang="en">
<head>
<meta charset="utf-8">
<title>Brightfold Systems Inc. — Software Development</title>
<link href="https://fonts.googleapis.com/css2?family=Poppins:wght@300;400;500;600;700&family=Roboto+Slab:wght@500&display=swap" rel="stylesheet">
<style>
:root{
  --navy:#0b1f5e;
  --navy-deep:#071a4d;
  --blue:#1b8fd8;
  --orange:#f06a24;
  --text:#2b2b2b;
  --muted:#555;
  --line:#d7dbe3;
  --map:#dfe6ee;
  --white:#fff;
}
*{margin:0;padding:0;box-sizing:border-box}
html,body{width:1200px;height:2171px;overflow:hidden;background:var(--white)}
body{position:relative;font-family:"Poppins",sans-serif;color:var(--text)}
.abs{position:absolute}
.btn{position:absolute;display:flex;align-items:center;justify-content:center;background:var(--navy);color:var(--white);font-weight:500}

/* header */
.brand{left:142px;top:14px;font-size:35px;font-weight:700;color:var(--navy);letter-spacing:-0.3px}
.header-phone{left:722px;top:28px;display:flex;align-items:center;gap:10px;color:var(--blue);font-size:15px}
.header-cta{left:862px;top:24px;width:198px;height:32px;font-size:15px}

/* hero */
.hero{left:0;top:83px;width:1200px;height:539px;background:radial-gradient(circle at 24% 30%,#3ec3ff 0,#1470c4 14%,#0d3a74 34%,#0a2a52 60%,#081d3a 100%)}
.hero-title{right:143px;top:230px;font-size:38px;color:var(--white);font-weight:400;text-align:right}
.hero-sub{right:143px;top:292px;width:480px;font-size:23px;line-height:36px;color:var(--white);font-weight:300;text-align:right}
.hero-cta{left:895px;top:414px;width:159px;height:37px;background:var(--orange);font-size:15px}

/* about */
.about-brand{left:150px;top:848px;width:300px;text-align:center;font-size:21px;font-weight:700;color:var(--navy)}
.about-divider{left:435px;top:712px;width:3px;height:209px;background:var(--navy)}
.about-heading{left:481px;top:690px;font-size:29px;line-height:35px;color:var(--navy)}
.about-heading span{color:var(--blue);display:block}
.about-text{left:481px;top:766px;width:530px;font-size:12.5px;line-height:24px;color:var(--text)}
.about-cta{left:482px;top:899px;width:109px;height:38px;font-size:14px}

/* services */
.services-heading{left:0;top:1060px;width:1200px;text-align:center;font-size:32px;color:var(--navy)}
.services-heading span{color:var(--blue)}
.services-intro{left:0;top:1110px;width:1200px;text-align:center;font-size:14px;color:var(--text)}
.service{position:absolute;top:1175px;width:270px;text-align:center}
.service-icon{width:96px;height:96px;margin:0 auto;border:3px solid var(--navy);border-radius:50%;display:flex;align-items:center;justify-content:center;background:#eef1f6;box-shadow:0 8px 8px -6px rgba(0,0,0,.2)}
.service-title{margin-top:26px;font-family:"Roboto Slab",serif;font-size:15px;font-weight:500;color:#111}
.service-text{margin-top:8px;font-size:12.5px;line-height:23px;color:var(--text)}
.services-cta{left:498px;top:1440px;width:197px;height:38px;font-size:15px;font-weight:600}

/* map */
.map{left:0;top:1542px;width:1200px;height:289px;background:linear-gradient(120deg,#e6ecf2,#d5dee8 45%,#e4eaf1)}
.map-pin{left:641px;top:1650px}
.map-card{left:708px;top:1631px;width:191px;height:80px;background:var(--navy);color:var(--white);padding:10px 12px;box-shadow:3px 4px 8px rgba(0,0,0,.3)}
.map-card strong{display:block;font-size:13.5px;font-weight:500}
.map-card p{font-size:12px;line-height:18px}

/* footer */
.footer-heading{top:1882px;font-size:14px;color:#222}
.contact-item{left:142px;display:flex;gap:14px;font-size:13px;line-height:19px;color:#222}
.abn{left:140px;top:2034px;font-size:15px;color:#222}
.abn b{color:var(--blue);font-weight:500}
.quick-links{left:505px;top:1921px;list-style:none;font-size:13px;line-height:26.5px;color:#222}
.field{position:absolute;border:1px solid var(--line);font-size:12px;color:#333;padding:8px 8px}
.submit{left:724px;top:2077px;width:126px;height:35px;font-size:17px;font-weight:600}
.social{top:2079px;width:27px;height:27px;border:1px solid var(--blue)}
.footer-name{left:278px;top:2068px;font-size:37px;font-weight:700;color:#e3eaf3}
.bottom-bar{left:0;top:2135px;width:1200px;height:36px;background:var(--navy-deep);color:var(--white);font-size:12.5px;display:flex;align-items:center;justify-content:center}
</style>
</head>
<body>

<header>
  <div class="abs brand">Brightfold Systems Inc.</div>
  <div class="abs header-phone">
    <svg width="20" height="20" viewBox="0 0 24 24" fill="none" stroke="#0b1f5e" stroke-width="1.8"><path d="M5 3h4l2 5-2.5 1.5a11 11 0 0 0 6 6L16 13l5 2v4a2 2 0 0 1-2 2A17 17 0 0 1 3 5a2 2 0 0 1 2-2z"/></svg>
    123.456.7890
  </div>
  <a class="btn header-cta">Get Your Solution Now!</a>
</header>

<section>
  <div class="abs hero" role="img" aria-label="Photo of an open hand holding a glowing blue digital globe on a dark blue background"></div>
  <h1 class="abs hero-title">We Develop All Kinds of</h1>
  <p class="abs hero-sub">Software From Web Applications, To Desktop Applications, To Mobile Applications</p>
  <a class="btn hero-cta">Let's Get Started</a>
</section>

<section>
  <div class="abs about-brand">Brightfold Systems Inc.</div>
  <div class="abs about-divider"></div>
  <svg class="abs" style="left:436px;top:804px" width="16" height="28" viewBox="0 0 16 28"><path d="M0 0 16 14 0 28z" fill="#0b1f5e"/></svg>
  <h2 class="abs about-heading">About<span>Our Mission</span></h2>
  <p class="abs about-text">Lorem ipsum dolor sit amet, consectetuer adipiscing elit, sed diam nonummy nibh euismod tincidunt ut laoreet dolore magna aliquam erat volutpat. Ut wisi enim ad minim veniam, quis nostrud exerci tation ullamcorper suscipit lobortis nisl ut aliquip ex ea commodo consequat. Duis autem vel eum iriure dolor in hendrerit in vulputate velit esse molestie consequat.</p>
  <a class="btn about-cta">Know More</a>
</section>

<section>
  <h2 class="abs services-heading">Our <span>Services</span></h2>
  <p class="abs services-intro">Lorem ipsum dolor sit amet, consectetuer adipiscing elit, sed diam nonummy nibh euismod.</p>

  <div class="service" style="left:140px">
    <div class="service-icon">
      <svg width="46" height="40" viewBox="0 0 46 40" fill="none" stroke="#0b1f5e" stroke-width="2"><rect x="6" y="4" width="34" height="24" fill="#cfe6f7"/><path d="M2 32h42v3H2z"/><path d="M18 12l-4 4 4 4M28 12l4 4-4 4M25 10l-4 12" stroke="#1b8fd8"/></svg>
    </div>
    <div class="service-title">Web Applications</div>
    <p class="service-text">Lorem ipsum dolor sit amet, sectetuer adipiscin ga mortis nisl aliquip fdafe ea commodo consequat. ....[+]</p>
  </div>

  <div class="service" style="left:460px">
    <div class="service-icon">
      <svg width="42" height="40" viewBox="0 0 42 40" fill="none" stroke="#0b1f5e" stroke-width="2"><rect x="3" y="3" width="36" height="24" fill="#cfe6f7"/><path d="M17 27v7M25 27v7M12 35h18"/><path d="M14 10h10M14 15h14M14 20h8" stroke="#1b8fd8"/></svg>
    </div>
    <div class="service-title">Desktop Applications</div>
    <p class="service-text">Lorem ipsum dolor sit amet, sectetuer adipiscin ga mortis nisl aliquip fdafe ea commodo consequat. ....[+]</p>
  </div>

  <div class="service" style="left:780px">
    <div class="service-icon">
      <svg width="44" height="46" viewBox="0 0 44 46" fill="none" stroke="#0b1f5e" stroke-width="2"><rect x="8" y="3" width="22" height="40" rx="3" fill="#cfe6f7"/><circle cx="19" cy="22" r="6" stroke="#1b8fd8"/><circle cx="19" cy="22" r="2" stroke="#1b8fd8"/><path d="M33 18h8M33 23h6M33 28h8"/></svg>
    </div>
    <div class="service-title">Mobile Applications</div>
    <p class="service-text">Lorem ipsum dolor sit amet, sectetuer adipiscin ga mortis nisl aliquip fdafe ea commodo consequat. ....[+]</p>
  </div>

  <a class="btn services-cta">Contact Us Today</a>
</section>

<section>
  <div class="abs map" role="img" aria-label="Muted road map of the office region"></div>
  <svg class="abs map-pin" width="30" height="38" viewBox="0 0 30 38" fill="none" stroke="#1b8fd8" stroke-width="2"><path d="M15 2a11 11 0 0 1 11 11c0 8-11 20-11 20S4 21 4 13A11 11 0 0 1 15 2z" fill="#fff"/><circle cx="15" cy="13" r="4"/><path d="M6 36h18"/></svg>
  <div class="abs map-card">
    <strong>Brightfold Systems Inc.</strong>
    <p>Street Name, City Name<br>US,&nbsp; NewYork 123458</p>
  </div>
</section>

<footer>
  <div class="abs footer-heading" style="left:142px">Contact Us</div>
  <div class="abs contact-item" style="top:1919px">
    <svg width="14" height="18" viewBox="0 0 14 18" fill="none" stroke="#1b8fd8" stroke-width="1.5"><path d="M7 1a6 6 0 0 1 6 6c0 4-6 10-6 10S1 11 1 7a6 6 0 0 1 6-6z"/><circle cx="7" cy="7" r="2"/></svg>
    <span>Street Name, City Name<br>US,&nbsp; NewYork 123458</span>
  </div>
  <div class="abs contact-item" style="top:1968px">
    <svg width="14" height="16" viewBox="0 0 24 24" fill="none" stroke="#1b8fd8" stroke-width="2"><path d="M5 3h4l2 5-2.5 1.5a11 11 0 0 0 6 6L16 13l5 2v4a2 2 0 0 1-2 2A17 17 0 0 1 3 5a2 2 0 0 1 2-2z"/></svg>
    <span>123.453.7890</span>
  </div>
  <div class="abs contact-item" style="top:1997px">
    <svg width="14" height="16" viewBox="0 0 14 16" fill="none" stroke="#1b8fd8" stroke-width="1.5"><rect x="1" y="3" width="12" height="9"/><path d="M1 3l6 5 6-5"/></svg>
    <span>inquiry@brightfoldsystems.com</span>
  </div>
  <div class="abs abn"><b>ABN:</b> 27 310 8842 5190</div>

  <div class="abs footer-heading" style="left:502px">Quick Links</div>
  <ul class="abs quick-links">
    <li>Home</li><li>About Us</li><li>Services</li><li>Team</li><li>Contact Us</li>
  </ul>

  <div class="abs footer-heading" style="left:721px">Contact Form</div>
  <div class="field" style="left:724px;top:1924px;width:334px;height:32px">First Name</div>
  <div class="field" style="left:724px;top:1961px;width:162px;height:32px">Email</div>
  <div class="field" style="left:892px;top:1961px;width:166px;height:32px">Phone</div>
  <div class="field" style="left:724px;top:1998px;width:334px;height:72px">Message</div>
  <a class="btn submit">Submit</a>

  <div class="abs social" style="left:139px"></div>
  <div class="abs social" style="left:174px"></div>
  <div class="abs social" style="left:209px"></div>
  <div class="abs footer-name">Brightfold Systems Inc.</div>

  <div class="abs bottom-bar">Copyright © 2019 Brightfold Systems Inc. All Rights Reserved | Privacy</div>
</footer>

</body>
</html>
```